Web Header needed for an inspirational coaching company's website - ongoing work

We need a beautifully designed web header to replace my current one at my homepage on my website www.kelvoria.com
There will be continuous work required for various creative work in the future if your work is selected.
I work with corporate professionals and executives to bring clarity and joy back to their career. It needs to be elegant, sophisticated, intelligent, but friendly and inspiring at the same time.
Thank you!
Target Market(s)
Corporate profesionals and executives
Industry/Entity Type
It Company
Colors
Designer to choose colors to be used in the design.
Look and feel

```html
<!DOCTYPE html>
<html lang="en">
<head>
<meta charset="utf-8">
<title>Bright Compass – Your Career Partner</title>
<link href="https://fonts.googleapis.com/css2?family=Oswald:wght@600&family=Caveat:wght@500&family=Cormorant+Garamond:wght@500&family=Arimo:wght@400;700&display=swap" rel="stylesheet">
<style>
  :root {
    --hero-bg: #c3c3c3;
    --hero-band: #9c9c9c;
    --navy: #363670;
    --ink: #222222;
    --body: #4a4a4a;
    --teal: #1d8c7c;
    --white: #ffffff;
    --nav: #f4f4f4;
  }
  * { margin: 0; padding: 0; box-sizing: border-box; }
  html, body { width: 1095px; height: 1200px; overflow: hidden; background: var(--white); }
  body { position: relative; font-family: "Arimo", Arial, sans-serif; color: var(--body); }

  .hero { position: absolute; left: 0; top: 0; width: 1095px; height: 410px;
    background: linear-gradient(180deg, #cdcdcd 0%, var(--hero-bg) 100%); }
  .hero-band { position: absolute; left: 0; top: 410px; width: 1095px; height: 16px; background: var(--hero-band); }

  .brand { position: absolute; left: 18px; top: 18px; color: var(--white);
    font-family: "Arimo", Arial, sans-serif; font-size: 15px; font-weight: 400; letter-spacing: 1px; line-height: 1.1; }

  .main-nav { position: absolute; top: 19px; left: 290px; display: flex; align-items: center;
    font-size: 10px; font-weight: 700; color: var(--nav); }
  .main-nav span { margin-right: 30px; }
  .nav-contact { position: absolute; left: 946px; top: 8px; width: 91px; height: 34px;
    border: 2px solid var(--white); border-radius: 17px; color: var(--white);
    font-size: 10px; font-weight: 400; display: flex; align-items: center; justify-content: center; }

  .hero-portrait { position: absolute; left: 160px; top: 75px; width: 290px; height: 335px;
    background: radial-gradient(ellipse at 50% 35%, #e6b99c 0%, #2a2020 45%, #e5562a 80%, #c3c3c3 100%); }

  .hero-title { position: absolute; left: 545px; top: 154px; font-family: "Oswald", sans-serif;
    font-weight: 600; font-size: 60px; color: var(--navy); letter-spacing: -1.5px; line-height: 1; transform: scaleX(0.92); transform-origin: left; }
  .hero-tagline { position: absolute; left: 572px; top: 222px; font-family: "Caveat", cursive;
    font-size: 38px; color: var(--ink); letter-spacing: 1px; }

  .welcome { position: absolute; left: 0; width: 1095px; top: 466px; text-align: center;
    font-family: "Cormorant Garamond", serif; font-size: 24px; color: var(--teal); letter-spacing: 0.5px; }
  .welcome-sub { position: absolute; left: 0; width: 1095px; top: 510px; text-align: center;
    font-size: 12px; font-weight: 700; color: var(--body); }

  .client-row { position: absolute; left: 160px; top: 562px; width: 770px; height: 44px;
    display: flex; justify-content: space-between; align-items: center; }
  .client { font-size: 14px; font-weight: 700; color: var(--ink); display: flex; align-items: center; gap: 5px; }
  .client i { display: inline-block; width: 10px; height: 10px; background: var(--ink); }

  .headline-quote { position: absolute; left: 0; width: 1095px; top: 634px; text-align: center;
    font-family: "Cormorant Garamond", serif; font-size: 24px; color: var(--teal); letter-spacing: 0.5px; }

  .intro { position: absolute; left: 160px; top: 690px; width: 380px; font-size: 12.2px; line-height: 19.5px; }
  .intro p { margin-bottom: 13px; }
  .intro a { color: var(--teal); text-decoration: none; }
  .intro .testimonial { font-weight: 700; color: var(--body); }

  .coach-photo { position: absolute; left: 636px; top: 690px; width: 227px; height: 240px;
    background: linear-gradient(160deg, #d7e6f6 0%, #9fc1ea 45%, #e5532b 100%); }
  .coach-caption { position: absolute; left: 636px; top: 956px; width: 230px; font-size: 10.5px; line-height: 14px; color: var(--body); }

  .feature { position: absolute; top: 1061px; width: 241px; height: 139px; }
  .feature-plan { left: 160px; background: linear-gradient(135deg, #fafafa, #e7d3c3); }
  .feature-workshop { left: 427px; background: linear-gradient(180deg, #eeeeee 0%, #c4423b 55%, #d8d8d8 100%); }
  .feature-vision { left: 695px; background: linear-gradient(180deg, #3f9fb0 0%, #8ab6b6 45%, #b98b4a 100%); }
</style>
</head>
<body>
  <header class="hero">
    <div class="brand">BRIGHT<br>COMPASS</div>
    <nav class="main-nav">
      <span>Home</span><span>About Mira</span><span>Testimonial</span><span>Methodology</span>
      <span>Coaching &amp; Mentoring</span><span>Workshop</span><span>Corporate</span><span>Blog</span>
    </nav>
    <div class="nav-contact">CONTACT</div>
    <div class="hero-portrait" role="img" aria-label="Portrait photo of the coach smiling, wearing an orange top"></div>
    <h1 class="hero-title">YOUR CAREER PARTNER</h1>
    <div class="hero-tagline">Bring Clarity to Your Career</div>
  </header>
  <div class="hero-band"></div>

  <h2 class="welcome">Welcome to Discover Your Bright Compass</h2>
  <p class="welcome-sub">A place for professionals &amp; executives to find clarity in their career</p>

  <div class="client-row">
    <span class="client"><i></i>Arvento</span>
    <span class="client">Telvana</span>
    <span class="client">Hexpoint</span>
    <span class="client">Lumora</span>
    <span class="client"><i></i>Mintpay</span>
    <span class="client">Qorvix</span>
    <span class="client">Delmar</span>
    <span class="client">Tixora</span>
    <span class="client"><i></i>Norbank</span>
  </div>

  <h2 class="headline-quote">"Best program I have ever attended in my career - Talia"</h2>

  <section class="intro">
    <p>Welcome! I am Mira Lenholt, I am known for helping professionals and executives find clarity in their career and life, so they can focus on what really matters and succeed with joy and meaning.</p>
    <p>In 2008, I was a senior executive with a young family seemingly had it all. However, I felt tired, unhappy and wanted to quit. At the end, I didn't quit, instead I began a search for an answer.</p>
    <p>I did extensive research over the years. What I found is that what I felt is normal and can be turned around with a simple approach.</p>
    <p>The approach gave me the direction, energy, made me a better leader and mum, and took me to a whole new level of joy, success, and career fulfilment. My greatest joy today is enabling others to do the same. <a href="#">Read my search and journey.</a></p>
    <p class="testimonial">"I know Mira is the best person to guide me on this journey. Mira makes you feel comfortable while pushing you to be your best - Oren, Director of Sales &amp; Alliances"</p>
  </section>

  <div class="coach-photo" role="img" aria-label="Photo of the coach speaking at a seminar with a headset microphone"></div>
  <p class="coach-caption">Mira Lenholt. Executive Coach. Fortune 100 Exec. Strength Psychology Expert. Mother.</p>

  <div class="feature feature-plan" role="img" aria-label="Photo of a hand ticking a checkbox with a pen"></div>
  <div class="feature feature-workshop" role="img" aria-label="Photo of a workshop group in a meeting room"></div>
  <div class="feature feature-vision" role="img" aria-label="Photo of hands framing a view of a sunny field"></div>
</body>
</html>
```